Book cover for ebook and Physical book for Mind Clutter Collective

I run a non-profit Mind Clutter Collective and I have a new book that needs a cover. For the physical book, I will need a full wrap. The mission is to help individuals Escape the cycle of restless inner chatter. This book is title is "Escape the cycle of restless inner chatter", and subtitle "Release Your Mind from Clutter." I am open to anything design wise, nothing is set in stone. Oh, MCC is pending Trademark.

Target Market(s)

Typically it's Mom's from 25-40

Industry/Entity Type

Mental Health

Font styles to use
Serif

Colors
f37122
9bcb3b
fbed22
0255a3
e34197

Requirements
Must have
• I do like simplicity, yet vibrant colors.
Nice to have
• The authors are Neil R. Dawkins, and Vera Holmquist. For some inspiration individuals refer to me as the Wonder Healer having reversed five incurable diseases.
Should not have
• The cover shouldn't be too busy.

```html
<!DOCTYPE html>
<html lang="en">
<head>
<meta charset="utf-8">
<title>Escape the cycle of restless inner chatter — Book Cover</title>
<link rel="stylesheet" href="https://fonts.googleapis.com/css2?family=Saira+Condensed:wght@300;400;600&family=Courgette&display=swap">
<style>
  :root {
    --stage: #0d1a29;
    --mauve-top: #9a5e63;
    --mauve-mid: #a8646a;
    --sunset-pink: #d9676a;
    --sunset-orange: #ee7a3f;
    --sunset-glow: #f9b45a;
    --band-white: #ffffff;
    --maroon: #5a2629;
    --title-ink: #efe6e6;
    --author-ink: #f3e9e9;
    --rule: rgba(255, 255, 255, 0.55);
    --badge-ink: #2a2a2a;
  }
  * { margin: 0; padding: 0; box-sizing: border-box; }
  html, body {
    width: 1200px;
    height: 800px;
    overflow: hidden;
    background: var(--stage);
  }
  .canvas {
    position: relative;
    width: 1200px;
    height: 800px;
  }
  .cover {
    position: absolute;
    left: 366px;
    top: 30px;
    width: 467px;
    height: 740px;
    overflow: hidden;
    background: linear-gradient(180deg, var(--mauve-top) 0%, var(--mauve-mid) 35%, var(--sunset-pink) 50%);
  }
  .cover__photo {
    position: absolute;
    left: 0;
    top: 240px;
    width: 100%;
    height: 350px;
    background:
      radial-gradient(ellipse 55% 40% at 50% 100%, var(--sunset-glow) 0%, rgba(249,180,90,0) 70%),
      linear-gradient(180deg, rgba(168,100,106,0) 0%, var(--sunset-pink) 30%, var(--sunset-orange) 70%, #f08a3e 100%);
  }
  .cover__title {
    position: absolute;
    right: 68px;
    top: 62px;
    font-family: "Saira Condensed", sans-serif;
    font-weight: 300;
    color: var(--title-ink);
    font-size: 54px;
    line-height: 62px;
    text-align: right;
    letter-spacing: -0.5px;
  }
  .cover__title-line { display: block; white-space: nowrap; }
  .cover__title-strong { font-weight: 600; }
  .cover__subtitle {
    position: absolute;
    left: 0;
    width: 100%;
    top: 326px;
    text-align: center;
    padding-left: 40px;
    font-family: "Courgette", cursive;
    font-size: 24px;
    color: var(--title-ink);
    white-space: nowrap;
  }
  .cover__band {
    position: absolute;
    left: 0;
    top: 590px;
    width: 100%;
    height: 7px;
    background: var(--band-white);
  }
  .cover__footer {
    position: absolute;
    left: 0;
    top: 597px;
    width: 100%;
    height: 143px;
    background: var(--maroon);
  }
  .cover__authors {
    position: absolute;
    left: 50%;
    top: 28px;
    transform: translateX(-50%);
    padding: 3px 2px;
    border-top: 1px solid var(--rule);
    border-bottom: 1px solid var(--rule);
    font-family: "Saira Condensed", sans-serif;
    font-weight: 400;
    font-size: 16px;
    color: var(--author-ink);
    white-space: nowrap;
  }
  .cover__badge {
    position: absolute;
    left: 50%;
    top: 64px;
    transform: translateX(-50%);
    padding: 0 10px;
    height: 36px;
    background: var(--band-white);
    display: flex;
    align-items: center;
    justify-content: center;
  }
  .cover__badge-name {
    font-family: "Saira Condensed", sans-serif;
    font-weight: 400;
    font-size: 13px;
    color: var(--badge-ink);
    line-height: 1;
    white-space: nowrap;
  }
</style>
</head>
<body>
  <main class="canvas">
    <article class="cover">
      <div class="cover__photo" role="img" aria-label="Photo of a woman with arms raised toward a glowing orange sunset over a grassy field"></div>

      <h1 class="cover__title">
        <span class="cover__title-line"><span class="cover__title-strong">Escape</span> the cycle of</span>
        <span class="cover__title-line"><span class="cover__title-strong">restless</span> inner</span>
        <span class="cover__title-line">chatter</span>
      </h1>

      <p class="cover__subtitle">Release Your Mind from Clutter</p>

      <div class="cover__band"></div>

      <footer class="cover__footer">
        <p class="cover__authors">Authors: Neil R. Dawkins and Vera Holmquist</p>
        <div class="cover__badge">
          <span class="cover__badge-name">Mind Clutter Collective</span>
        </div>
      </footer>
    </article>
  </main>
</body>
</html>
```